Church Music Album Cover

We are a Christian church in the OKC metro that is releasing a CD of songs that have connected with our congregation over the past few years. We are a church of about 1500 people of all ages- so while we want the design to be fresh, clean, and attractive- it doesn't have to be overly "youthy" or "edgy." Per the CD distribution company, the art image file you create should be able to be delivered with these requirements met:1400 x 1400 pixels minimum; 3000 x 3000 pixels maximumPNG, GIF, JPG, or JPEG file type72 - 300dpi (300dpi is the best)Less than 25mbRGB color scheme (not CMYK)
Updates

Thanks for submissions thus far. I realize my initial description may have not been the most helpful- and it some ways, I'm not 100% sure what I want. However, I would typically end to stay away from concrete images and tend to lean more towards earthy folk images. I don't even know if that makes sense. One google image search of the word "Grace" brings up individual letters spelling out Grace- each on a card clothes lined to a rope with out of focus lights or candles in the background. Another one had out of focus patio light bulbs lighting up the general text. Not sure why I like those and how they can connect to the theme, but I do. Another one had "Grace" on a pallet wall type background. Hopefully those are helpful suggestions.

Target Market(s)

Young parents- 30-40's

Colors

Requirements
Must have
• Title: Melodies from the River Stone
Nice to have
• Earthy/folky themes.
Should not have
• Bright colors

```html
<!DOCTYPE html>
<html lang="en">
<head>
<meta charset="utf-8">
<title>Melodies from the River Stone</title>
<link rel="stylesheet" href="https://fonts.googleapis.com/css2?family=Playfair+Display:ital,wght@1,500&display=swap">
<style>
  :root {
    --sky-deep: #4c6664;
    --sky-mid: #6f8781;
    --sky-light: #a9ada0;
    --haze: #e8dfcf;
    --cloud-clay: #c49b86;
    --cloud-glow: #eddac8;
    --title: #fbf6ee;
  }
  html, body {
    margin: 0;
    padding: 0;
    width: 1200px;
    height: 1200px;
    overflow: hidden;
    background: var(--sky-deep);
  }
  .album-cover {
    position: relative;
    width: 1200px;
    height: 1200px;
    overflow: hidden;
  }
  .sky-photo {
    position: absolute;
    inset: 0;
    background:
      radial-gradient(ellipse 260px 210px at 620px 600px, var(--cloud-glow) 0%, rgba(196,155,134,0.85) 45%, rgba(196,155,134,0) 100%),
      radial-gradient(ellipse 110px 60px at 660px 370px, rgba(196,155,134,0.7) 0%, rgba(196,155,134,0) 100%),
      radial-gradient(ellipse 130px 100px at 100px 560px, rgba(214,190,170,0.45) 0%, rgba(214,190,170,0) 100%),
      radial-gradient(ellipse 950px 280px at 600px 1150px, var(--haze) 0%, rgba(232,223,207,0.7) 45%, rgba(232,223,207,0) 100%),
      linear-gradient(180deg, var(--sky-deep) 0%, var(--sky-mid) 45%, var(--sky-light) 80%, var(--haze) 100%);
  }
  .album-title {
    position: absolute;
    top: 62px;
    left: 0;
    width: 100%;
    margin: 0;
    text-align: center;
    font-family: "Playfair Display", Georgia, serif;
    font-style: italic;
    font-weight: 500;
    font-size: 100px;
    line-height: 128px;
    color: var(--title);
    letter-spacing: 1px;
  }
  .album-title .title-line {
    display: block;
  }
</style>
</head>
<body>
  <main class="album-cover">
    <div class="sky-photo" role="img" aria-label="Photograph of a soft, muted sky with a glowing warm cloud at the centre and pale haze along the bottom"></div>
    <h1 class="album-title">
      <span class="title-line">Melodies from the</span>
      <span class="title-line">River Stone</span>
    </h1>
  </main>
</body>
</html>
```